Expanding Training Company needs a powerpoint template to deliver a consistent professional image

We want to start with a ppt template that is clean and flexible.
We are a small training organisation focusing on personal effectiveness, leadership, management and change. The MD is a New Zealander living in the United Kingdom and loves the idea of the clean green image that NZ has and wants the PowerPoint template to reflect that. We are pragmatic in what we do - everything comes back to performance improvement. Our clients are big players and our presentations need to be as clean, and as professional as theirs. We need a template that is versatile and can have their logos added as necessary.
Our training tends to be very current and as such we would like to use a lot of images and less words/bullets. We have company colours, logos and fonts that we are happy with and will continue to use.

Here are our company values to give you a sense of what we are about…

As a learning organisation we are always looking to continually improve and renew, our material, ideas, and methods, and are continually on the look out for new techniques, interventions and applications that provide measurable results to our clients.

We think life is about people and relationships, and we are prepared to walk away if people don't keep their word, are untrustworthy or lack integrity, as life is just too short to work with arses.
And because we are not arses we admit when we are wrong and make good on our commitments.

For our clients its all about performance and training is a performance enhancer, we aim to provide training excellence tin all its guises that delivers performance and happy clients.

We harness the value of the team, we believe in Interdependence.

We make life easier for our clients and each other.

Flexibility, innovation and future focus/vision are what our clients can count on us for.

Work is one of many of life's great facilitators, we recognise and value the others - its not just about work.

Industry/Entity Type

It Company

Other font styles liked:
• Avenir Next

Colors
abd037
9bcb3c

Requirements
Must have
• A clean look with multiple options for inserting images, tables, videos, text boxes etc
• copyright information
Nice to have
• Slide masters

```html
<!DOCTYPE html>
<html lang="en">
<head>
<meta charset="utf-8">
<title>Verdant Consulting – Presentation Template Overview</title>
<link rel="stylesheet" href="https://fonts.googleapis.com/css2?family=Nunito+Sans:wght@300;400;600;700;800&display=swap">
<style>
:root{
  --green:#1f9e45;
  --green-dark:#138a3a;
  --lime:#9bcb3c;
  --lime-2:#abd037;
  --lime-bright:#8ccf1e;
  --orange:#f07c1a;
  --grey-band:#5f6269;
  --grey-text:#8a8d92;
  --grey-light:#e6e7e8;
  --ink:#3f4247;
  --page:#e4e5e6;
  --white:#ffffff;
  --photo-cool:linear-gradient(135deg,#cfd6dc,#8d9aa6);
  --photo-warm:linear-gradient(135deg,#e6ddd3,#a89c90);
}
*{box-sizing:border-box;margin:0;padding:0}
html,body{width:1200px;height:858px;overflow:hidden;background:var(--page)}
body{font-family:"Nunito Sans",Arial,sans-serif;color:var(--ink);position:relative}
.slide{position:absolute;width:291px;height:164px;background:var(--white);overflow:hidden}
.abs{position:absolute}
.corner{position:absolute;top:6px;right:9px;width:0;height:0;border-top:5px solid var(--orange);border-left:5px solid transparent}
.pnum{position:absolute;top:3px;right:4px;font-size:3px;color:var(--grey-text)}
.ttl{position:absolute;font-size:7.2px;font-weight:300;color:var(--grey-text);letter-spacing:.2px;text-transform:uppercase}
.ttl b{font-weight:700;color:var(--ink)}
.ttl.on-green,.ttl.on-green b{color:var(--white)}
.txt{position:absolute;font-size:4px;line-height:5.4px;color:var(--grey-text);text-align:justify}
.ticks{position:absolute;list-style:none;font-size:3.8px;line-height:6.4px;color:var(--grey-text)}
.ticks li::before{content:"✓";color:var(--orange);margin-right:4px;font-weight:700}
.ph{position:absolute;background:var(--photo-cool)}
.ph.warm{background:var(--photo-warm)}
.brand{position:absolute;display:flex;align-items:center;gap:3px;font-size:7px;font-weight:600;color:var(--green)}
.brand i{display:block;width:8px;height:8px;border-radius:50%;background:var(--green)}
.circ{position:absolute;border-radius:50%}
</style>
</head>
<body>

<!-- Row 1 -->
<section class="slide" style="left:8px;top:6px">
  <div class="ph" style="left:0;top:0;width:150px;height:164px" role="img" aria-label="Portrait of a smiling consultant holding a clipboard"></div>
  <svg class="abs" style="left:0;top:0" width="291" height="164"><defs><linearGradient id="g1" x1="0" y1="0" x2="1" y2="1"><stop offset="0" stop-color="#7cc24a"/><stop offset="1" stop-color="#1f9e45"/></linearGradient></defs>
    <polygon points="140,0 291,0 291,164 92,164" fill="url(#g1)"/>
    <polygon points="150,138 236,138 226,164 140,164" fill="#137a35"/>
    <polygon points="236,138 291,138 291,164 226,164" fill="#fff"/>
  </svg>
  <div class="abs" style="left:155px;top:62px;color:#fff;font-size:7px;font-weight:800;line-height:8px">PERFORMANCE IMPROVEMENT<br><span style="font-weight:400">WITH VERDANT CONSULTING</span></div>
  <div class="abs" style="left:155px;top:82px;color:#fff;font-size:4px;line-height:6px">MAR 2017<br>PRESENTED BY : <b>JORDAN VALE</b></div>
  <div class="abs" style="left:170px;top:153px;color:#d7eec0;font-size:3px">www.verdantconsult.example</div>
  <div class="brand" style="left:238px;top:146px;font-size:5.5px"><i style="width:6px;height:6px"></i>verdant</div>
</section>

<section class="slide" style="left:305px;top:6px">
  <div class="abs" style="left:0;top:0;width:291px;height:105px;background:linear-gradient(180deg,#6db04a,#2e9a45)" role="img" aria-label="City skyline with a rocket launching in green tones"></div>
  <svg class="abs" style="left:0;top:0" width="291" height="164"><path d="M0,100 C30,70 70,80 90,92 C120,72 160,76 180,95 C210,75 250,72 291,92 L291,164 L0,164Z" fill="#fff"/><rect x="0" y="161" width="291" height="3" fill="var(--green)"/></svg>
  <div class="abs" style="left:115px;top:113px;font-size:6.8px;font-weight:800;color:var(--green-dark);line-height:7.5px">PERFORMANCE IMPROVEMENT<br><span style="font-weight:400">WITH VERDANT CONSULTING</span></div>
  <div class="abs" style="left:115px;top:131px;font-size:3.6px;color:var(--grey-text)">PRESENTED BY: <span style="color:var(--orange)">JORDAN VALE</span></div>
  <div class="abs" style="left:115px;top:143px;width:74px;height:8px;background:var(--green);color:#fff;font-size:3.6px;text-align:center;line-height:8px">MAR 2017</div>
  <div class="brand" style="left:10px;top:147px;font-size:6px"><i style="width:6px;height:6px"></i>verdant</div>
</section>

<section class="slide" style="left:602px;top:6px">
  <div class="abs" style="left:0;top:0;width:135px;height:164px;background:linear-gradient(135deg,#7fc25a,#2fa14a)" role="img" aria-label="Team meeting photo with green overlay"></div>
  <div class="ttl on-green" style="left:15px;top:10px"><b>CONTENT</b> AT GLANCE</div>
  <div class="txt" style="left:22px;top:66px;width:80px;color:#eaf6df">Real leaders are people who help us overcome the limits of our own fear and doubt, and who push us to do our best work every day.</div>
  <div class="abs" style="left:120px;top:0;width:16px;height:164px;background:var(--green-dark);font-size:3.4px;color:#fff;line-height:11.8px;text-align:center;padding-top:44px">01<br>02<br>03<br>04<br>05<br>06<br>07<br>08</div>
  <div class="abs" style="left:148px;top:47px;width:123px;font-size:4px;line-height:11.8px;color:var(--ink)">
    <div style="display:flex;justify-content:space-between;border-bottom:.5px solid var(--grey-light)"><span>Self-Awareness</span><span>01</span></div>
    <div style="display:flex;justify-content:space-between;border-bottom:.5px solid var(--grey-light)"><span>Professional Integrity</span><span>02</span></div>
    <div style="display:flex;justify-content:space-between;border-bottom:.5px solid var(--grey-light)"><span>Leadership In The Entry Level</span><span>03</span></div>
    <div style="display:flex;justify-content:space-between;border-bottom:.5px solid var(--grey-light)"><span>Trust, Accountability &amp; Reliability</span><span>04</span></div>
    <div style="display:flex;justify-content:space-between;border-bottom:.5px solid var(--grey-light)"><span>The Value of Questions</span><span>05</span></div>
    <div style="display:flex;justify-content:space-between;border-bottom:.5px solid var(--grey-light)"><span>Owning Mistakes</span><span>06</span></div>
    <div style="display:flex;justify-content:space-between;border-bottom:.5px solid var(--grey-light)"><span>Resilience In The Face of Challenges</span><span>07</span></div>
    <div style="display:flex;justify-content:space-between"><span>Utilizing Your Strengths</span><span>08</span></div>
  </div>
  <div class="corner"></div>
</section>

<section class="slide" style="left:900px;top:6px">
  <div class="ttl" style="left:14px;top:11px"><b>WELCOME</b> FROM OUR COMPANY</div>
  <div class="txt" style="left:14px;top:24px;width:262px;text-align:left">Cum sociis natoque penatibus et magnis dis parturient montes, nascetur ridiculus mus. Donec quam felis, ultricies nec, pellentesque eu, pretium quis, sem.</div>
  <div class="ph" style="left:30px;top:57px;width:66px;height:44px" role="img" aria-label="Colleagues talking in an office"></div>
  <div class="ph warm" style="left:108px;top:57px;width:66px;height:44px" role="img" aria-label="Hands working at a desk with laptop"></div>
  <div class="ph" style="left:186px;top:57px;width:66px;height:44px" role="img" aria-label="Business presenter in a suit"></div>
  <div class="txt" style="left:55px;top:117px;width:180px;text-align:center;font-size:3.4px;line-height:4.6px">Vivamus elementum semper nisi. Aenean vulputate eleifend tellus. Aenean leo ligula, porttitor eu, consequat vitae, eleifend ac, enim. Aliquam lorem ante, dapibus in, viverra quis, feugiat a, tellus.</div>
  <div class="corner"></div>
</section>

<!-- Row 2 -->
<section class="slide" style="left:8px;top:176px">
  <div class="ph" style="left:0;top:0;width:121px;height:164px" role="img" aria-label="Businesswoman standing in a bright office"></div>
  <div class="ttl" style="left:131px;top:26px"><b>WHY ARE</b> YOU HERE</div>
  <div class="txt" style="left:131px;top:40px;width:146px">Cras at malesuada ipsum. Ut vestibulum, erat quis dictum consequat, eros ante bibendum nisl, non interdum erat tortor et odio.</div>
  <ul class="ticks" style="left:131px;top:64px">
    <li>Personalize Contact Requests</li><li>Have a professional profile picture</li><li>Always be professional</li><li>Make your contact list open to all connections</li><li>Introduce Connections to each other</li><li>Respond promptly to messages</li>
  </ul>
  <div class="txt" style="left:131px;top:112px;width:146px">Cras at malesuada ipsum. Ut vestibulum, erat quis dictum consequat, eros ante bibendum nisl, non interdum erat tortor et odio.</div>
  <div class="corner"></div>
</section>

<section class="slide" style="left:305px;top:176px">
  <div class="ttl" style="left:14px;top:11px"><b>FIVE KEY</b> SUCCESSFUL</div>
  <div class="txt" style="left:14px;top:23px;width:262px;text-align:left">Cum sociis natoque penatibus et magnis dis parturient montes, nascetur ridiculus mus. Donec quam felis, ultricies nec, pellentesque eu, pretium quis, sem.</div>
  <div class="abs" style="left:0;top:45px;width:291px;height:32px;background:var(--grey-band)"></div>
  <div class="abs" style="left:14px;top:61px;width:262px;height:.6px;background:#9aa0a6"></div>
  <div class="circ" style="left:12px;top:59px;width:4px;height:4px;background:#fff"></div>
  <div class="abs" style="left:270px;top:58px;width:0;height:0;border-left:4px solid #fff;border-top:3px solid transparent;border-bottom:3px solid transparent"></div>
  <div style="position:absolute;left:0;top:0">
    <div class="circ" style="left:34px;top:51px;width:20px;height:20px;background:#fff;border:1.5px solid var(--orange)"></div>
    <div class="circ" style="left:88px;top:51px;width:20px;height:20px;background:#fff;border:1.5px solid var(--orange)"></div>
    <div class="circ" style="left:142px;top:51px;width:20px;height:20px;background:#fff;border:1.5px solid var(--orange)"></div>
    <div class="circ" style="left:196px;top:51px;width:20px;height:20px;background:#fff;border:1.5px solid var(--orange)"></div>
    <div class="circ" style="left:250px;top:51px;width:20px;height:20px;background:#fff;border:1.5px solid var(--orange)"></div>
  </div>
  <div class="abs" style="left:13px;top:88px;width:264px;display:flex;gap:5px;font-size:3.6px;color:#fff;text-align:center;line-height:7px">
    <span style="flex:1;background:var(--green-dark)">ORGANIZED</span><span style="flex:1;background:var(--green)">READABLE</span><span style="flex:1;background:#5db33a">CONCISE</span><span style="flex:1;background:var(--lime)">ATTRACTIVE</span><span style="flex:1;background:var(--lime-2)">INTERESTING</span>
  </div>
  <div class="abs" style="left:13px;top:98px;width:264px;display:flex;gap:5px;font-size:3.3px;line-height:5.4px;color:var(--grey-text)">
    <span style="flex:1">• Vulputate eleifend<br>• Tellus. Aenean leo<br>• Ligula, porttitor eu<br>• Vulputate eleifend</span>
    <span style="flex:1">Lorem ipsum dolor sit amet, consectetuer adipiscing elit. Aenean commodo ligula eget dolor.</span>
    <span style="flex:1">• Vulputate eleifend<br>• Tellus. Aenean leo<br>• Ligula, porttitor eu<br>• Vulputate eleifend</span>
    <span style="flex:1">Lorem ipsum dolor sit amet, consectetuer adipiscing elit. Aenean commodo ligula eget dolor.</span>
    <span style="flex:1">• Vulputate eleifend<br>• Tellus. Aenean leo<br>• Ligula, porttitor eu<br>• Vulputate eleifend</span>
  </div>
  <div class="corner"></div>
</section>

<section class="slide" style="left:602px;top:176px">
  <div class="ttl" style="left:14px;top:11px"><b>SIX KEY</b> SUCCESSFUL</div>
  <div class="abs" style="left:12px;top:36px;width:95px;text-align:right;font-size:3.3px;line-height:4.4px;color:var(--grey-text)">
    <div style="color:var(--lime);font-size:4.6px;line-height:6px">BEKERJA KERAS</div>Nunc luctus porttitor magna efficitur venenatis. Phasellus maximus mauris at pulvinar mollis.
    <div style="color:var(--lime);font-size:4.6px;line-height:6px;margin-top:15px">LEMBUR TERUS</div>Nunc luctus porttitor magna efficitur venenatis. Phasellus maximus mauris at pulvinar mollis.
    <div style="color:var(--lime);font-size:4.6px;line-height:6px;margin-top:15px">JARANG JAJAN</div>Nunc luctus porttitor magna efficitur venenatis. Phasellus maximus mauris at pulvinar mollis.
  </div>
  <div class="circ" style="left:113px;top:45px;width:14px;height:14px;background:var(--grey-light)"></div>
  <div class="circ" style="left:113px;top:79px;width:14px;height:14px;background:var(--grey-light)"></div>
  <div class="circ" style="left:113px;top:113px;width:14px;height:14px;background:var(--grey-light)"></div>
  <div class="circ" style="left:165px;top:45px;width:14px;height:14px;background:var(--grey-light)"></div>
  <div class="circ" style="left:165px;top:79px;width:14px;height:14px;background:var(--grey-light)"></div>
  <div class="circ" style="left:165px;top:113px;width:14px;height:14px;background:var(--grey-light)"></div>
  <div class="abs" style="left:207px;top:36px;width:70px;font-size:3.3px;line-height:4.4px;color:var(--grey-text)">
    <div style="color:var(--lime);font-size:4.6px;line-height:6px">ANTI DUGEM</div>Nunc luctus porttitor magna efficitur venenatis. Phasellus maximus mauris at pulvinar mollis.
    <div style="color:var(--lime);font-size:4.6px;line-height:6px;margin-top:15px">ANTI MIRAS</div>Nunc luctus porttitor magna efficitur venenatis. Phasellus maximus mauris at pulvinar mollis.
    <div style="color:var(--lime);font-size:4.6px;line-height:6px;margin-top:15px">SUKSES DAH</div>Nunc luctus porttitor magna efficitur venenatis. Phasellus maximus mauris at pulvinar mollis.
  </div>
  <div class="corner"></div>
</section>

<section class="slide" style="left:900px;top:176px">
  <div class="ttl" style="left:14px;top:11px"><b>STRENGTHS MATCH</b> ICON LIST</div>
  <div style="position:absolute;inset:0;font-size:3.8px;text-align:center">
    <div class="circ" style="left:72px;top:37px;width:22px;height:22px;border:.8px solid var(--grey-light)"></div><div class="circ" style="left:77px;top:42px;width:12px;height:12px;background:var(--green)"></div>
    <div class="circ" style="left:138px;top:37px;width:22px;height:22px;border:.8px solid var(--grey-light)"></div><div class="circ" style="left:143px;top:42px;width:12px;height:12px;background:var(--green)"></div>
    <div class="circ" style="left:204px;top:37px;width:22px;height:22px;border:.8px solid var(--grey-light)"></div><div class="circ" style="left:209px;top:42px;width:12px;height:12px;background:var(--lime)"></div>
    <div class="circ" style="left:72px;top:81px;width:22px;height:22px;border:.8px solid var(--grey-light)"></div><div class="circ" style="left:77px;top:86px;width:12px;height:12px;background:var(--green)"></div>
    <div class="circ" style="left:138px;top:81px;width:22px;height:22px;border:.8px solid var(--grey-light)"></div><div class="circ" style="left:143px;top:86px;width:12px;height:12px;background:var(--lime)"></div>
    <div class="circ" style="left:204px;top:81px;width:22px;height:22px;border:.8px solid var(--grey-light)"></div><div class="circ" style="left:209px;top:86px;width:12px;height:12px;background:var(--lime-2)"></div>
    <span class="abs" style="left:58px;top:63px;width:50px;color:var(--green)">Marketing Strategies</span>
    <span class="abs" style="left:124px;top:63px;width:50px;color:var(--lime)">Budgetary Overview</span>
    <span class="abs" style="left:190px;top:63px;width:50px;color:#bfc4c8">Future Projections</span>
    <span class="abs" style="left:58px;top:107px;width:50px;color:var(--green)">Training Methods</span>
    <span class="abs" style="left:124px;top:107px;width:50px;color:var(--lime)">Planning The Company</span>
    <span class="abs" style="left:190px;top:107px;width:50px;color:#bfc4c8">Redesigning Website</span>
  </div>
  <div class="corner"></div>
</section>

<!-- Row 3 -->
<section class="slide" style="left:8px;top:346px">
  <div class="ph warm" style="left:0;top:0;width:140px;height:164px;background:linear-gradient(135deg,#f3f3f3,#cfc8c0)" role="img" aria-label="Hand writing with a pen on paper"></div>
  <div class="ttl" style="left:138px;top:26px"><b>DISCUSS</b> THE FOLLOWING QUESTIONS</div>
  <div class="txt" style="left:141px;top:40px;width:138px">Cras at malesuada ipsum. Ut vestibulum, erat quis dictum consequat, eros ante bibendum nisl, non interdum erat tortor et odio.</div>
  <ul class="ticks" style="left:145px;top:66px;color:var(--ink);font-size:4px;line-height:7px"><li>Personalize Contact Requests?</li><li>Have a professional profile picture?</li><li>Always be professional?</li></ul>
  <div class="txt" style="left:141px;top:92px;width:138px">Cras at malesuada ipsum. Ut vestibulum, erat quis dictum consequat, eros ante bibendum nisl, non interdum erat tortor et odio.</div>
  <div class="corner"></div>
</section>

<section class="slide" style="left:305px;top:346px">
  <div class="abs" style="left:0;top:0;width:92px;height:164px;background:linear-gradient(180deg,#39a83a,#69b81f)"></div>
  <div class="ttl on-green" style="left:6px;top:37px;font-size:6.6px"><b style="color:#fff">LEADERSHIP</b> <span style="color:var(--ink)">PURPOSE</span></div>
  <div class="txt" style="left:7px;top:64px;width:80px;color:#eef8e2">Real leaders are people who help us overcome the limits of our own individual laziness and selfishness and weakness and fear, and get us to do better, harder things than we can get ourselves to do on our own.</div>
  <div class="ph" style="left:92px;top:0;width:74px;height:164px" role="img" aria-label="Businesswoman in a blazer looking down"></div>
  <div class="abs" style="left:194px;top:56px;width:80px;font-size:3.6px;line-height:4.8px;color:var(--grey-text)">
    <p style="margin-bottom:14px"><span style="color:var(--orange)">▸</span>&nbsp; Praesent commodo vitae eros id sollicitudin</p>
    <p style="margin-bottom:14px"><span style="color:var(--orange)">▸</span>&nbsp; Lorem ipsum dolor sit amet, consectetuer adipiscing elit</p>
    <p><span style="color:var(--orange)">▸</span>&nbsp; Cum sociis natoque penatibus et magnis dis parturient montes</p>
  </div>
  <div class="corner"></div>
</section>

<section class="slide" style="left:602px;top:346px">
  <div class="ttl" style="left:14px;top:15px"><b>PERSONAL</b> COMMUNICATION</div>
  <div class="txt" style="left:14px;top:29px;width:126px">Cras at malesuada ipsum. Ut vestibulum, erat quis dictum consequat, eros ante bibendum nisl, non interdum erat tortor et odio.</div>
  <ul class="ticks" style="left:20px;top:54px;line-height:6.2px;font-size:3.5px"><li>Personalize Contact Requests</li><li>Have a professional profile picture</li><li>Always be professional</li><li>Make your contact list open to all connections</li><li>Introduce Connections to each other</li><li>Respond promptly to messages</li></ul>
  <div class="txt" style="left:14px;top:102px;width:126px">Cras at malesuada ipsum. Ut vestibulum, erat quis dictum consequat, eros ante bibendum nisl, non interdum erat tortor et odio.</div>
  <div class="ph" style="left:145px;top:0;width:146px;height:164px" role="img" aria-label="Smiling businessman in a meeting"></div>
  <div class="circ" style="left:139px;top:77px;width:12px;height:12px;background:#fff;border:.6px solid var(--grey-light)"></div>
</section>

<section class="slide" style="left:900px;top:346px">
  <div class="ph" style="left:150px;top:0;width:141px;height:164px" role="img" aria-label="Confident businessman gesturing while speaking"></div>
  <svg class="abs" style="left:0;top:0" width="291" height="164">
    <polygon points="160,0 180,0 150,164 130,164" fill="#9aa0a6" opacity=".35"/>
    <polygon points="42,64 190,64 175,164 0,164 0,105" fill="var(--green)"/>
  </svg>
  <div class="abs" style="left:8px;top:6px;font-size:6.6px;color:var(--grey-text);line-height:8px">THE NEXT LEVEL OF<br><b style="color:var(--ink)">LEADERSHIP</b></div>
  <div class="txt" style="left:81px;top:27px;width:80px;text-align:left;font-size:4.4px;line-height:6px">Leadership and learning are indispensable to each other</div>
  <div class="abs" style="left:0;top:0;color:#fff">
    <div class="abs" style="left:49px;top:72px;width:120px;display:flex;gap:6px;align-items:center"><b style="font-size:9px">01</b><span style="font-size:3.6px;line-height:4.8px">Cum sociis natoque penatibus et magnis dis parturient montes.</span></div>
    <div class="abs" style="left:39px;top:95px;width:120px;display:flex;gap:6px;align-items:center"><b style="font-size:9px">02</b><span style="font-size:3.6px;line-height:4.8px">Cum sociis natoque penatibus et magnis dis parturient montes.</span></div>
    <div class="abs" style="left:29px;top:118px;width:120px;display:flex;gap:6px;align-items:center"><b style="font-size:9px">03</b><span style="font-size:3.6px;line-height:4.8px">Cum sociis natoque penatibus et magnis dis parturient montes.</span></div>
    <div class="abs" style="left:19px;top:141px;width:120px;display:flex;gap:6px;align-items:center"><b style="font-size:9px">04</b><span style="font-size:3.6px;line-height:4.8px">Cum sociis natoque penatibus et magnis dis parturient montes.</span></div>
  </div>
  <div class="corner"></div>
</section>

<!-- Row 4 -->
<section class="slide" style="left:8px;top:516px">
  <div class="ttl" style="left:102px;top:29px;font-size:8.2px"><b>INSPIRING</b> PEOPLE</div>
  <div class="txt" style="left:35px;top:61px;width:220px;text-align:center;font-size:3.5px;line-height:5px">We all have people who inspire us in our lives, both personally and professionally. Looking at well known achievers, what is the first thing you think of for each? What is one thing that inspires you about each?</div>
  <div class="abs" style="left:0;top:82px;width:291px;height:82px;display:grid;grid-template-columns:repeat(6,1fr);grid-template-rows:1fr 1fr">
    <div style="background:var(--photo-cool)" role="img" aria-label="Portrait of an inspiring leader"></div>
    <div style="background:var(--photo-warm)" role="img" aria-label="Portrait of an inspiring leader"></div>
    <div style="background:var(--lime-bright);color:#fff;font-size:3px;line-height:4.5px;padding:8px 3px">Evan Hale<br>Nora Pike</div>
    <div style="background:var(--photo-cool)" role="img" aria-label="Portrait of an inspiring leader"></div>
    <div style="background:var(--photo-warm)" role="img" aria-label="Portrait of an inspiring leader"></div>
    <div style="background:var(--green);color:#fff;font-size:3px;line-height:4.5px;padding:8px 3px"><b>Liam Grove</b><br>June Marlow<br>Theo Brandt</div>
    <div style="background:var(--green);color:#fff;font-size:3px;line-height:4.5px;padding:6px 3px"><b>Carl Denning</b><br>Ruth Ashby<br>Felix Moray</div>
    <div style="background:var(--photo-cool)" role="img" aria-label="Portrait of an inspiring leader"></div>
    <div style="background:var(--photo-warm)" role="img" aria-label="Portrait of an inspiring leader"></div>
    <div style="background:var(--orange)"></div>
    <div style="background:var(--lime-bright)"></div>
    <div style="background:var(--green)"></div>
  </div>
  <div class="corner"></div>
</section>

<section class="slide" style="left:305px;top:516px">
  <div class="ttl" style="left:14px;top:11px"><b>YOUR STRENGTHS</b> INFOGRAPHIC</div>
  <div class="txt" style="left:14px;top:23px;width:262px;text-align:left">Cum sociis natoque penatibus et magnis dis parturient montes, nascetur ridiculus mus. Donec quam felis, ultricies nec, pellentesque eu, pretium quis, sem.</div>
  <div class="abs" style="left:110px;top:48px;width:66px;height:108px;background:linear-gradient(180deg,#e9ecef,#c9ced3);border-radius:4px" role="img" aria-label="Illustration of a presenter pointing upward"></div>
  <div class="abs" style="left:40px;top:58px;font-size:9.5px;font-weight:700;color:var(--lime)">3 Times</div>
  <div class="txt" style="left:40px;top:73px;width:60px;text-align:left;font-size:3px;line-height:4px;color:#b5b8bc">Vestibulum lobortis, libero vel gravida pretium, nisl vel dapibus.</div>
  <div class="abs" style="left:40px;top:106px;font-size:9.5px;font-weight:700;color:var(--lime)">6 Times</div>
  <div class="txt" style="left:40px;top:121px;width:60px;text-align:left;font-size:3px;line-height:4px;color:#b5b8bc">Vestibulum lobortis, libero vel gravida pretium, nisl vel dapibus.</div>
  <div class="abs" style="left:196px;top:58px;font-size:9.5px;font-weight:700;color:var(--ink)">With 8%</div>
  <div class="txt" style="left:196px;top:73px;width:60px;text-align:left;font-size:3px;line-height:4px;color:#b5b8bc">Vestibulum lobortis, libero vel gravida pretium, nisl vel dapibus.</div>
  <div class="abs" style="left:196px;top:106px;font-size:9.5px;font-weight:700;color:var(--ink)">Over 15%</div>
  <div class="txt" style="left:196px;top:121px;width:60px;text-align:left;font-size:3px;line-height:4px;color:#b5b8bc">Vestibulum lobortis, libero vel gravida pretium, nisl vel dapibus.</div>
  <div class="corner"></div>
</section>

<section class="slide" style="left:602px;top:516px;background:radial-gradient(circle at 50% 55%,#5cc13f,#189a3d 75%)">
  <div class="ttl on-green" style="left:14px;top:11px"><b>VISUALIZING</b> YOUR LEADERSHIP</div>
  <svg class="abs" style="left:0;top:0" width="291" height="164" fill="none" stroke="#d9f0c9" stroke-width=".6" stroke-dasharray="1.5 1.5">
    <line x1="145" y1="64" x2="145" y2="86"/><line x1="92" y1="83" x2="126" y2="83"/><line x1="164" y1="83" x2="198" y2="83"/><line x1="92" y1="116" x2="126" y2="116"/><line x1="164" y1="116" x2="198" y2="116"/>
    <circle cx="145" cy="57" r="5.5" stroke-dasharray="none"/><circle cx="92" cy="83" r="5.5" stroke-dasharray="none"/><circle cx="209" cy="83" r="5.5" stroke-dasharray="none"/><circle cx="92" cy="116" r="5.5" stroke-dasharray="none"/><circle cx="209" cy="116" r="5.5" stroke-dasharray="none"/>
  </svg>
  <div class="abs" style="left:132px;top:74px;width:28px;height:70px;background:linear-gradient(180deg,rgba(255,255,255,.35),rgba(255,255,255,.1));border-radius:4px" role="img" aria-label="Illustration of a standing business figure"></div>
  <div class="abs" style="left:112px;top:30px;width:66px;text-align:center;font-size:3.4px;line-height:4.4px;color:#e9f7dd"><b style="color:#fff">WHERE</b><br>Phasellus maximus mauris at pulvinar mollis.</div>
  <div class="abs" style="left:20px;top:76px;width:64px;text-align:right;font-size:3.4px;line-height:4.4px;color:#e9f7dd"><b style="color:#fff">WITH</b><br>Phasellus maximus mauris at pulvinar mollis.</div>
  <div class="abs" style="left:20px;top:109px;width:64px;text-align:right;font-size:3.4px;line-height:4.4px;color:#e9f7dd"><b style="color:#fff">WHAT</b><br>Phasellus maximus mauris at pulvinar mollis.</div>
  <div class="abs" style="left:219px;top:76px;width:62px;font-size:3.4px;line-height:4.4px;color:#e9f7dd"><b style="color:#fff">WHAT</b><br>Phasellus maximus mauris at pulvinar mollis.</div>
  <div class="abs" style="left:219px;top:109px;width:62px;font-size:3.4px;line-height:4.4px;color:#e9f7dd"><b style="color:#fff">HOW</b><br>Phasellus maximus mauris at pulvinar mollis.</div>
  <div class="pnum" style="color:#dff3cf">15</div>
</section>

<section class="slide" style="left:900px;top:516px">
  <div class="ttl" style="left:14px;top:11px"><b>THE PROCESS</b></div>
  <svg class="abs" style="left:0;top:0" width="291" height="164">
    <polygon points="4,80 48,80 54,89 48,98 4,98" fill="var(--green)"/>
    <polygon points="48,80 88,80 94,89 88,98 48,98 54,89" fill="var(--green)" opacity=".9"/>
    <polygon points="88,80 128,80 134,89 128,98 88,98 94,89" fill="#36a93d"/>
    <polygon points="128,80 168,80 174,89 168,98 128,98 134,89" fill="#5ab52e"/>
    <polygon points="168,80 208,80 214,89 208,98 168,98 174,89" fill="var(--lime)"/>
    <polygon points="208,80 248,80 254,89 248,98 208,98 214,89" fill="var(--orange)"/>
    <polygon points="248,80 282,80 288,89 282,98 248,98 254,89" fill="var(--grey-band)"/>
    <g fill="none" stroke="#a9adb2" stroke-width=".7"><rect x="47" y="36" width="10" height="12"/><circle cx="131" cy="41" r="4.5"/><line x1="128" y1="44" x2="124" y2="49"/><rect x="211" y="40" width="9" height="8"/><rect x="8" y="105" width="10" height="10" rx="5"/><line x1="90" y1="115" x2="98" y2="106"/><ellipse cx="169" cy="110" rx="6" ry="4.5"/><rect x="242" y="105" width="10" height="10"/></g>
  </svg>
  <div class="abs" style="left:4px;top:86px;width:284px;display:flex;font-size:3.4px;color:#fff;text-align:center">
    <span style="width:44px">EXECUTE</span><span style="width:40px">REVIEW</span><span style="width:40px">INDICATE</span><span style="width:40px">IDENTIFY</span><span style="width:40px">CHECKING</span><span style="width:40px">CONFIRM</span><span style="width:40px">DEALS</span>
  </div>
  <div class="abs" style="left:46px;top:52px;font-size:3.3px;line-height:4.3px;color:var(--ink)">Vestibulum<br>lobortis, libero vel<br>gravida pretium</div>
  <div class="abs" style="left:124px;top:52px;font-size:3.3px;line-height:4.3px;color:var(--ink)">Vestibulum<br>lobortis, libero vel<br>gravida pretium</div>
  <div class="abs" style="left:202px;top:52px;font-size:3.3px;line-height:4.3px;color:var(--ink)">Vestibulum<br>lobortis, libero vel<br>gravida pretium</div>
  <div class="abs" style="left:7px;top:120px;font-size:3.3px;line-height:4.3px;color:var(--ink)">Vestibulum<br>lobortis, libero vel<br>gravida pretium</div>
  <div class="abs" style="left:86px;top:120px;font-size:3.3px;line-height:4.3px;color:var(--ink)">Vestibulum<br>lobortis, libero vel<br>gravida pretium</div>
  <div class="abs" style="left:164px;top:120px;font-size:3.3px;line-height:4.3px;color:var(--ink)">Vestibulum<br>lobortis, libero vel<br>gravida pretium</div>
  <div class="abs" style="left:242px;top:120px;font-size:3.3px;line-height:4.3px;color:var(--ink)">Vestibulum<br>lobortis, libero vel<br>gravida pretium</div>
  <div class="corner"></div>
</section>

<!-- Row 5 -->
<section class="slide" style="left:8px;top:686px">
  <div class="ttl" style="left:14px;top:11px"><b>TRAINING</b> PROCESS</div>
  <svg class="abs" style="left:0;top:0" width="291" height="164">
    <rect x="6" y="79" width="92" height="11" fill="var(--green)"/><polygon points="98,79 104,84.5 98,90" fill="#222"/>
    <rect x="104" y="79" width="92" height="11" fill="#3aaa3a"/><polygon points="196,79 202,84.5 196,90" fill="#222"/>
    <rect x="202" y="79" width="85" height="11" fill="var(--lime)"/><polygon points="287,79 291,84.5 287,90" fill="#222"/>
    <g fill="none" stroke="var(--ink)" stroke-width=".7"><path d="M12,56 h4 v-5 l3,-4 1,1 -1,4 h5 v8 h-12z"/><path d="M210,51 v12 M215,51 v12 M220,51 v12"/><rect x="208" y="54" width="4" height="2"/><rect x="213" y="58" width="4" height="2"/><rect x="218" y="55" width="4" height="2"/><ellipse cx="120" cy="101" rx="6" ry="2"/><path d="M114,101 v8 a6,2 0 0 0 12,0 v-8"/></g>
  </svg>
  <div class="abs" style="left:11px;top:83px;font-size:3.5px;color:#fff">DEAL SOURCING</div>
  <div class="abs" style="left:109px;top:83px;font-size:3.5px;color:#fff">EXECUTIVE SOURCING</div>
  <div class="abs" style="left:207px;top:83px;font-size:3.5px;color:#fff">INVESTMENT PROCESS</div>
  <div class="txt" style="left:12px;top:64px;width:82px;text-align:left;color:var(--ink);font-size:3.3px;line-height:4.2px">Cras at malesuada ipsum. Ut vestibulum, erat quis dictum consequat, eros ante bibendum nisl, non interdum erat tortor et odio.</div>
  <div class="txt" style="left:202px;top:64px;width:82px;text-align:left;color:var(--ink);font-size:3.3px;line-height:4.2px">Cras at malesuada ipsum. Ut vestibulum, erat quis dictum consequat, eros ante bibendum nisl, non interdum erat tortor et odio.</div>
  <div class="txt" style="left:105px;top:113px;width:82px;text-align:left;color:var(--ink);font-size:3.3px;line-height:4.2px">Cras at malesuada ipsum. Ut vestibulum, erat quis dictum consequat, eros ante bibendum nisl, non interdum erat tortor et odio.</div>
  <div class="corner"></div>
</section>

<section class="slide" style="left:305px;top:686px">
  <div class="ttl" style="left:14px;top:11px"><b>TRAINING</b> PROCESS</div>
  <svg class="abs" style="left:0;top:0" width="291" height="164">
    <rect x="8" y="77" width="63" height="10" fill="var(--green)"/><polygon points="71,77 76,82 71,87" fill="#222"/>
    <rect x="76" y="77" width="63" height="10" fill="var(--lime-bright)"/><polygon points="139,77 144,82 139,87" fill="#222"/>
    <rect x="144" y="77" width="63" height="10" fill="var(--orange)"/><polygon points="207,77 212,82 207,87" fill="#222"/>
    <rect x="212" y="77" width="63" height="10" fill="#a3a6ab"/>
    <g fill="none" stroke="var(--ink)" stroke-width=".7"><path d="M84,50 l4,-3 3,2 5,-5"/><rect x="85" y="46" width="2" height="5" fill="var(--ink)"/><rect x="89" y="45" width="2" height="6" fill="var(--ink)"/><circle cx="222" cy="47" r="4.5"/><circle cx="222" cy="47" r="1.8"/><path d="M24,105 a4.5,4.5 0 1 1 1,3"/><rect x="161" y="103" width="12" height="8"/><line x1="161" y1="106" x2="173" y2="106"/></g>
  </svg>
  <div class="abs" style="left:12px;top:80px;font-size:3.5px;color:#fff">INVESTORS</div>
  <div class="abs" style="left:80px;top:80px;font-size:3.5px;color:#fff">OVERSIGHT</div>
  <div class="abs" style="left:148px;top:80px;font-size:3.5px;color:#fff">INVESTMENT</div>
  <div class="abs" style="left:216px;top:80px;font-size:3.5px;color:#fff">LIQUIDITY</div>
  <div class="txt" style="left:80px;top:57px;width:58px;text-align:left;color:var(--ink);font-size:3.3px;line-height:4.2px">Morbi libero nulla, convallis et quam et, condimentum fringilla ligula.</div>
  <div class="txt" style="left:215px;top:57px;width:58px;text-align:left;color:var(--ink);font-size:3.3px;line-height:4.2px">Morbi libero nulla, convallis et quam et, condimentum fringilla ligula.</div>
  <div class="txt" style="left:10px;top:126px;width:58px;text-align:left;color:var(--ink);font-size:3.3px;line-height:4.2px">Morbi libero nulla, convallis et quam et, condimentum fringilla ligula.</div>
  <div class="txt" style="left:146px;top:126px;width:58px;text-align:left;color:var(--ink);font-size:3.3px;line-height:4.2px">Morbi libero nulla, convallis et quam et, condimentum fringilla ligula.</div>
  <div class="corner"></div>
</section>

<section class="slide" style="left:602px;top:686px">
  <div class="ttl" style="left:14px;top:11px"><b>EXECUTIVE</b> ADVISORY BOARD</div>
  <div class="abs" style="left:0;top:37px;width:291px;height:127px;display:grid;grid-template-columns:repeat(3,1fr);grid-template-rows:1fr 1fr;gap:8px 0">
    <div style="display:flex"><div style="width:44px;background:var(--lime-bright);position:relative"><div class="circ" style="left:8px;top:10px;width:28px;height:28px;background:var(--photo-cool);border:1.5px solid #fff" role="img" aria-label="Board member portrait"></div></div><div style="padding:4px 3px;font-size:3.2px;line-height:4.2px;color:var(--grey-text)"><b style="font-size:5.2px;color:var(--ink)">Aria Whitlow</b><br>• CEO and Clerk<br>• Founder or Senior Executive</div></div>
    <div style="display:flex"><div style="width:44px;background:var(--green);position:relative"><div class="circ" style="left:8px;top:10px;width:28px;height:28px;background:var(--photo-warm);border:1.5px solid #fff" role="img" aria-label="Board member portrait"></div></div><div style="padding:4px 3px;font-size:3.2px;line-height:4.2px;color:var(--grey-text)"><b style="font-size:5.2px;color:var(--ink)">Dario Kent</b><br>• Finance Advisor<br>• Founder/Chairman &amp; CEO</div></div>
    <div style="display:flex"><div style="width:44px;background:var(--green);position:relative"><div class="circ" style="left:8px;top:10px;width:28px;height:28px;background:var(--photo-cool);border:1.5px solid #fff" role="img" aria-label="Board member portrait"></div></div><div style="padding:4px 3px;font-size:3.2px;line-height:4.2px;color:var(--grey-text)"><b style="font-size:5.2px;color:var(--ink)">Milo Harker</b><br>• Former member of Oldschool Group<br>• Senior Executive</div></div>
    <div style="display:flex"><div style="width:44px;background:var(--lime-bright);position:relative"><div class="circ" style="left:8px;top:10px;width:28px;height:28px;background:var(--photo-warm);border:1.5px solid #fff" role="img" aria-label="Board member portrait"></div></div><div style="padding:4px 3px;font-size:3.2px;line-height:4.2px;color:var(--grey-text)"><b style="font-size:5.2px;color:var(--ink)">Tomas Reyne</b><br>• Senior Trainer<br>• Founder or Senior Executive</div></div>
    <div style="display:flex"><div style="width:44px;background:var(--green);position:relative"><div class="circ" style="left:8px;top:10px;width:28px;height:28px;background:var(--photo-cool);border:1.5px solid #fff" role="img" aria-label="Board member portrait"></div></div><div style="padding:4px 3px;font-size:3.2px;line-height:4.2px;color:var(--grey-text)"><b style="font-size:5.2px;color:var(--ink)">Lena Orwell</b><br>• Trainer<br>• Senior Executive</div></div>
    <div style="display:flex"><div style="width:44px;background:var(--green);position:relative"><div class="circ" style="left:8px;top:10px;width:28px;height:28px;background:var(--photo-cool);border:1.5px solid #fff" role="img" aria-label="Board member portrait"></div></div><div style="padding:4px 3px;font-size:3.2px;line-height:4.2px;color:var(--grey-text)"><b style="font-size:5.2px;color:var(--ink)">Owen Castell</b><br>• Board Director<br>• Founder &amp; Senior Executive</div></div>
  </div>
  <div class="corner"></div>
</section>

<section class="slide" style="left:900px;top:686px;background:var(--green)">
  <div class="abs" style="left:97px;top:0;width:90px;height:150px;background:#fff"></div>
  <div class="abs" style="left:97px;top:60px;width:90px;text-align:center;font-size:9px;font-weight:800;color:#707378">THANK YOU</div>
  <div class="abs" style="left:97px;top:74px;width:90px;text-align:center;font-size:3.4px;color:var(--lime)">Please contact us for more information</div>
  <div class="brand" style="left:128px;top:133px;font-size:6px"><i style="width:6px;height:6px"></i>verdant</div>
  <div class="abs" style="left:105px;top:155px;font-size:3.2px;color:#fff;display:flex;gap:14px"><span>✉ hello@vc.example</span><span>✆ 0-000-0000</span></div>
</section>

</body>
</html>
```